Wordpress Design and Coding for New Residential and Commercial Lawn and Landscape Co.

I need a Wordpress site with coding built for a startup Residential and Commercial Lawn and Landscape Company. I'm uploading our business card and logo files. I'd like a really clean design, with icons to describe services and who we serve. We don't have a lot of content being new.
We offer a large variety of services. Our 2 target customers would be residential and commercial. We offer the following services: Lawn Care and Mowing, Hedge and Shrub Trimming, Removal and Clean Up, Aeration and Sod, Mulch and Rock Installation, Landscape Installations and Renovations, and Commercial Snow Removal in the winter for Retail Shopping Centers, Communities, and other larger customers.
We serve Baltimore County, Harford County, and Surrounding areas.
Target Market(s)
We have 2 main types of customer.
1. Residential - this includes lawn maintenance, plantings, mulch & rock installs, and maintenance, etc.
2. Commercial - this includes complete care from design, planting, maintenance, etc. Communities, Property Managers, Housing Associations, Shopping Centers, Retail, etc.
Industry/Entity Type
Landscape
Coding
Coded - Design and coding required
Requirements
Must have
- Clean design. Nice distinct icons to display services and other information. Large Bold eye popping landscape photo at top.
- I've included screen shots of designs I like. Please do not copy them, they are competitors.
Nice to have
- 1. Link to our Facebook page - fb.com/brightfurrowmd
- 2. Link to FB Photos for Gallery Section - https://www.example-social.com/pg/BrightFurrowMD/photos/
- 3. Why Choose Us section.
- 4. Contact form that includes 4 sections - Name, Phone #, Service Address, and Comments.
- 5. Reviews/Testimonials on Landing Page

```html
<!DOCTYPE html>
<html lang="en">
<head>
<meta charset="utf-8">
<title>Bright Furrow Lawn &amp; Landscape</title>
<link rel="stylesheet" href="https://fonts.googleapis.com/css2?family=Oswald:wght@500&family=Montserrat:wght@300;400;500;600;700&family=Poppins:wght@300;400;500&display=swap">
<style>
:root{
  --green:#8dc021;
  --green-dark:#6f9e12;
  --ink:#1c1c1c;
  --text:#555;
  --muted:#777;
  --line:#d8d8d8;
  --panel:#f3f3f3;
  --slate:#616161;
  --footer:#151515;
  --footer-bar:#0e0e0e;
  --white:#fff;
}
*{margin:0;padding:0;box-sizing:border-box}
html,body{width:1200px;height:3495px;overflow:hidden}
body{position:relative;background:var(--white);font-family:"Poppins",sans-serif;color:var(--text)}
.abs{position:absolute}
a{color:inherit;text-decoration:none}

.topbar{left:0;top:0;width:1200px;height:23px;background:var(--green)}
.topbar .dots{left:112px;top:6px;display:flex;gap:14px}
.topbar .dots span{width:10px;height:10px;border-radius:50%;background:var(--white)}
.topbar .phone{right:112px;top:2px;color:var(--white);font-size:14px;font-weight:500;display:flex;align-items:center;gap:6px}

.nav{left:0;top:23px;width:1200px;height:70px;background:var(--white);z-index:3}
.brand{left:116px;top:8px;width:150px;height:110px;background:var(--white);display:flex;flex-direction:column;align-items:center;justify-content:center;gap:8px;z-index:4;box-shadow:0 2px 4px rgba(0,0,0,.08)}
.brand .mark{width:42px;height:42px;border-radius:50%;background:var(--green)}
.brand .name{font-family:"Montserrat",sans-serif;font-weight:700;font-size:15px;color:var(--green-dark);text-align:center;line-height:1.2}
.menu{left:575px;top:24px;display:flex;gap:40px;font-family:"Montserrat",sans-serif;font-size:14px;font-weight:500;color:var(--ink)}
.menu .current{color:var(--green)}

.hero{left:0;top:93px;width:1200px;height:470px;background:linear-gradient(100deg,#6a5a44 0%,#8a7658 28%,#5b6a3a 52%,#3f6e22 75%,#2f5a18 100%)}
.hero-curve{left:0;top:530px;width:1200px;height:40px}
.hero h1{left:0;top:262px;width:1200px;text-align:center;font-family:"Oswald",sans-serif;font-weight:500;font-size:50px;color:var(--white);letter-spacing:1px}
.hero .sub{left:0;top:322px;width:1200px;text-align:center;font-family:"Montserrat",sans-serif;font-size:26px;font-weight:500;color:var(--white)}
.btn-outline{border:2px solid var(--white);color:var(--white);font-family:"Montserrat",sans-serif;font-size:12px;font-weight:600;display:flex;align-items:center;justify-content:center;letter-spacing:.5px}
.hero .btn-outline{left:506px;top:391px;width:186px;height:49px;font-size:14px}

.audience{top:566px;width:488px;height:219px}
.audience.residential{left:112px;background:linear-gradient(180deg,#4a5040 0%,#2b2f27 100%)}
.audience.commercial{left:600px;background:linear-gradient(180deg,rgba(141,192,33,.85),rgba(120,175,20,.95)),#6c8a3a}
.audience h2{position:absolute;left:42px;top:80px;font-family:"Montserrat",sans-serif;font-weight:600;font-size:26px;color:var(--white);letter-spacing:.5px}
.audience p{position:absolute;left:42px;top:114px;font-size:13px;color:var(--white)}
.audience .btn-outline{position:absolute;left:44px;top:150px;width:100px;height:35px;font-size:11px;border-width:1px}

.section-title{left:0;width:1200px;text-align:center;font-family:"Montserrat",sans-serif;font-weight:500;font-size:33px;color:var(--ink)}
.section-sub{left:0;width:1200px;text-align:center;font-size:13px;color:var(--muted)}

.service{width:300px;text-align:center}
.service .icon{display:block;margin:0 auto}
.service h3{margin-top:22px;font-family:"Montserrat",sans-serif;font-weight:400;font-size:17px;color:#333}

.why-band{left:0;top:1720px;width:1200px;height:661px;background:var(--panel)}
.point{left:112px;width:470px}
.point .badge{position:absolute;left:0;top:0;width:66px;height:66px;border-radius:50%;background:var(--green);border:5px solid #dfe9c8}
.point .bracket{position:absolute;left:33px;top:66px;width:250px;height:90px;border-left:2px solid var(--green);border-bottom:2px solid var(--green)}
.point .num{position:absolute;left:42px;top:135px;font-size:13px;color:#333}
.point h4{position:absolute;left:87px;top:-2px;font-family:"Montserrat",sans-serif;font-weight:500;font-size:17px;color:#333;line-height:1.35}
.point h4 span{display:block;color:var(--green)}
.point p{position:absolute;left:87px;top:52px;width:380px;font-size:12px;line-height:1.6;color:var(--muted)}

.why-box{left:617px;top:1682px;width:471px;height:741px;background:var(--slate);color:var(--white)}
.why-box h2{position:absolute;left:47px;top:50px;font-family:"Montserrat",sans-serif;font-weight:500;font-size:33px}
.why-box p{position:absolute;left:47px;width:380px;font-size:11.5px;line-height:1.6;color:#eee}
.why-photo{position:absolute;left:42px;top:396px;width:385px;height:294px;background:var(--white);padding:16px}
.why-photo div{width:100%;height:100%;background:linear-gradient(160deg,#5f8f35,#3c6a1e 55%,#7aa64b)}

.quote{left:270px;top:2630px;width:660px;text-align:center;font-size:12.5px;font-style:italic;line-height:2.1;color:#555}
.arrow{top:2690px}
.avatar{left:547px;top:2724px;width:106px;height:106px;border-radius:50%;border:5px solid var(--green);background:linear-gradient(160deg,#cda98f,#8f6a55)}
.person{left:0;top:2840px;width:1200px;text-align:center;font-size:13px;color:#444}

.lawn-band{left:0;top:2924px;width:1200px;height:245px;background:linear-gradient(180deg,#ffffff 0%,#bfe08a 25%,#6fb02a 55%,#4c8f1c 100%)}
.lawn-band h2{position:absolute;left:112px;top:140px;font-family:"Montserrat",sans-serif;font-size:32px;font-weight:700;color:var(--white)}
.lawn-band h2 span{font-weight:400}
.lawn-band p{position:absolute;left:112px;top:184px;font-size:13px;font-weight:500;color:var(--white)}
.lawn-band .btn-outline{position:absolute;left:972px;top:168px;width:102px;height:32px;font-size:11px;border-width:1px}

.footer{left:0;top:3169px;width:1200px;height:249px;background:var(--footer);color:#bbb}
.footer h5{position:absolute;top:55px;font-family:"Poppins",sans-serif;font-weight:400;font-size:20px;color:#ddd}
.footer .rule{position:absolute;top:90px;height:1px;background:#333}
.links{position:absolute;left:112px;top:100px;list-style:none;font-size:12px;line-height:23px}
.links li::before{content:"›";margin-right:10px;color:#888}
.contact{position:absolute;left:347px;top:96px;font-size:12px;line-height:1.6;width:230px}
.contact .row{display:flex;gap:12px;margin-bottom:12px;align-items:flex-start}
.contact svg{flex:none;margin-top:2px}
.map{position:absolute;left:597px;top:100px;width:188px;height:117px;background:linear-gradient(135deg,#d9e4d0,#b9cde0)}
.news p{position:absolute;left:876px;top:96px;width:220px;font-size:12px;line-height:1.5}
.news .field{position:absolute;left:874px;top:133px;width:214px;height:35px;background:var(--white);color:#999;font-size:11px;padding:10px 10px}
.news .submit{position:absolute;left:874px;top:182px;width:102px;height:30px;background:var(--green);color:var(--white);font-size:11px;font-weight:600;display:flex;align-items:center;justify-content:center}
.footer-bar{left:0;top:3418px;width:1200px;height:77px;background:var(--footer-bar);border-top:1px solid #2a2a2a}
.social{position:absolute;left:112px;top:22px;display:flex;gap:14px}
.social span{width:34px;height:34px;border-radius:50%;border:2px solid #ddd}
.copy{position:absolute;right:112px;top:30px;font-size:12px;color:#bbb}
</style>
</head>
<body>

<header>
  <div class="abs topbar">
    <div class="abs dots"><span></span><span></span><span></span><span></span></div>
    <div class="abs phone">
      <svg width="14" height="14" viewBox="0 0 24 24"><circle cx="12" cy="12" r="11" fill="none" stroke="#fff" stroke-width="2"/><path d="M8 6l2 3-1.5 1.5a8 8 0 0 0 5 5L15 14l3 2-1 2.5C11 18 6 13 5.5 7z" fill="#fff"/></svg>
      555.014.2290
    </div>
  </div>
  <div class="abs nav">
    <nav class="abs menu">
      <a class="current" href="#">Home</a><a href="#">About Us</a><a href="#">Services</a><a href="#">Testimonials</a><a href="#">Contact Us</a>
    </nav>
  </div>
  <a class="abs brand" href="#"><span class="mark"></span><span class="name">Bright Furrow<br>Lawn &amp; Landscape</span></a>
</header>

<section>
  <div class="abs hero" role="img" aria-label="Photo of a curved stone garden wall with flowers beside a freshly mown lawn"></div>
  <svg class="abs hero-curve" viewBox="0 0 1200 40" preserveAspectRatio="none"><path d="M0 35 Q600 -25 1200 35 L1200 40 L0 40 Z" fill="#fff"/></svg>
  <h1 class="abs hero-title" style="position:absolute" >MAKE YOUR LAWN</h1>
  <p class="abs sub" style="position:absolute;left:0;top:322px;width:1200px;text-align:center;font-family:'Montserrat',sans-serif;font-size:26px;font-weight:500;color:#fff">Clean &amp; Beautiful</p>
  <a class="abs btn-outline" href="#" style="left:506px;top:391px;width:186px;height:49px;font-size:14px">CONTACT US NOW</a>
</section>
<style>.hero-title{left:0;top:262px;width:1200px;text-align:center;font-family:"Oswald",sans-serif;font-weight:500;font-size:50px;color:#fff;letter-spacing:1px}</style>

<section>
  <div class="abs audience residential" role="img" aria-label="Photo of a suburban house at dusk">
    <h2>RESIDENTIAL</h2><p>Lorem ipsum, we don't agree.</p><a class="btn-outline" href="#">KNOW MORE</a>
  </div>
  <div class="abs audience commercial" role="img" aria-label="Photo of a landscaped commercial garden path with green overlay">
    <h2>COMMERCIAL</h2><p>Lorem ipsum, we don't agree.</p><a class="btn-outline" href="#">KNOW MORE</a>
  </div>
</section>

<section>
  <h2 class="abs section-title" style="top:862px">FEATURED SERVICES</h2>
  <p class="abs section-sub" style="top:912px">Active investment management tailored to your unique needs and goals</p>

  <div class="abs service" style="left:122px;top:987px">
    <svg class="icon" width="100" height="100" viewBox="0 0 100 100"><circle cx="50" cy="50" r="44" fill="none" stroke="#ddd" stroke-width="10"/><rect x="34" y="46" width="32" height="14" rx="3" fill="#8dc021"/><circle cx="38" cy="64" r="5" fill="#8dc021"/><circle cx="62" cy="64" r="5" fill="#8dc021"/><path d="M38 46 L30 30" stroke="#8dc021" stroke-width="3"/></svg>
    <h3>Lawn Care and Mowing</h3>
  </div>
  <div class="abs service" style="left:449px;top:987px">
    <svg class="icon" width="100" height="100" viewBox="0 0 100 100"><circle cx="50" cy="50" r="44" fill="none" stroke="#ddd" stroke-width="10"/><path d="M40 28 L58 62 M60 28 L42 62" stroke="#8dc021" stroke-width="5"/><circle cx="40" cy="68" r="5" fill="#8dc021"/><circle cx="60" cy="68" r="5" fill="#8dc021"/></svg>
    <h3>Hedge and Shrub Trimming</h3>
  </div>
  <div class="abs service" style="left:775px;top:987px">
    <svg class="icon" width="100" height="100" viewBox="0 0 100 100"><circle cx="50" cy="50" r="44" fill="none" stroke="#ddd" stroke-width="10"/><path d="M62 30 L44 54" stroke="#8dc021" stroke-width="4"/><path d="M36 50 l12 10 -8 10 -12 -10z" fill="#8dc021"/></svg>
    <h3>Removal and Clean Up</h3>
  </div>

  <div class="abs service" style="left:122px;top:1208px">
    <svg class="icon" width="100" height="100" viewBox="0 0 100 100"><circle cx="50" cy="50" r="44" fill="none" stroke="#ddd" stroke-width="10"/><ellipse cx="42" cy="42" rx="7" ry="11" fill="#8dc021" transform="rotate(-40 42 42)"/><ellipse cx="60" cy="48" rx="7" ry="11" fill="#8dc021" transform="rotate(60 60 48)"/><ellipse cx="46" cy="62" rx="7" ry="11" fill="#8dc021" transform="rotate(10 46 62)"/></svg>
    <h3>Aeration and Sod</h3>
  </div>
  <div class="abs service" style="left:449px;top:1208px">
    <svg class="icon" width="100" height="100" viewBox="0 0 100 100"><circle cx="50" cy="50" r="44" fill="none" stroke="#ddd" stroke-width="10"/><path d="M34 64 Q50 46 66 64 Z" fill="#8dc021"/><path d="M48 28 L54 52" stroke="#8dc021" stroke-width="4"/></svg>
    <h3>Mulch and Rock Installation</h3>
  </div>
  <div class="abs service" style="left:775px;top:1208px">
    <svg class="icon" width="100" height="100" viewBox="0 0 100 100"><circle cx="50" cy="50" r="44" fill="none" stroke="#ddd" stroke-width="10"/><circle cx="46" cy="38" r="6" fill="#8dc021"/><path d="M30 64 L50 48 L70 58 L66 64 Z" fill="#8dc021"/></svg>
    <h3>Landscape Install and Renovations</h3>
  </div>

  <div class="abs service" style="left:122px;top:1441px">
    <svg class="icon" width="100" height="100" viewBox="0 0 100 100"><circle cx="50" cy="50" r="44" fill="none" stroke="#ddd" stroke-width="10"/><circle cx="46" cy="36" r="6" fill="#8dc021"/><path d="M42 44 L54 44 L58 62 L36 66 Z" fill="#8dc021"/><path d="M56 46 L68 34" stroke="#8dc021" stroke-width="4"/></svg>
    <h3>Snow Removal</h3>
  </div>
  <div class="abs service" style="left:449px;top:1441px">
    <svg class="icon" width="100" height="100" viewBox="0 0 100 100"><circle cx="50" cy="50" r="44" fill="none" stroke="#ddd" stroke-width="10"/><g stroke="#8dc021" stroke-width="4" stroke-linecap="round"><path d="M50 30v40M32 40l36 20M32 60l36-20"/></g></svg>
    <h3>Winter Maintenance</h3>
  </div>
  <div class="abs service" style="left:775px;top:1441px">
    <svg class="icon" width="100" height="100" viewBox="0 0 100 100"><circle cx="50" cy="50" r="44" fill="none" stroke="#ddd" stroke-width="10"/><circle cx="50" cy="46" r="14" fill="#8dc021"/><rect x="47" y="56" width="6" height="14" fill="#8dc021"/></svg>
    <h3>Tree Care</h3>
  </div>
</section>

<section>
  <div class="abs why-band"></div>

  <div class="abs point" style="top:1771px">
    <span class="badge"></span><span class="bracket"></span><span class="num">01</span>
    <h4>We are Professional<span>Landscapist</span></h4>
    <p>Lorem ipsum dolor sit amet, consectetuer adipiscing elit, sed diam nonummy nibh euismod tincidunt ut laoreet dolore magna aliquam erat volutpat.</p>
  </div>
  <div class="abs point" style="top:1966px">
    <span class="badge"></span><span class="bracket"></span><span class="num">02</span>
    <h4>Quality &amp; Reliability<span>Work</span></h4>
    <p>Lorem ipsum dolor sit amet, consectetuer adipiscing elit, sed diam nonummy nibh euismod tincidunt ut laoreet dolore magna aliquam erat volutpat.</p>
  </div>
  <div class="abs point" style="top:2166px">
    <span class="badge"></span><span class="bracket"></span><span class="num">03</span>
    <h4>100 % Trusted<span>Team Member</span></h4>
    <p>Lorem ipsum dolor sit amet, consectetuer adipiscing elit, sed diam nonummy nibh euismod tincidunt ut laoreet dolore magna aliquam erat volutpat.</p>
  </div>

  <div class="abs why-box">
    <h2>WHY CHOOSE US</h2>
    <p style="top:112px">Lorem ipsum dolor sit amet, consectetuer adipiscing elit, sed diam nonummy nibh euismod tincidunt ut laoreet dolore magna aliquam erat volutpat.</p>
    <p style="top:186px">Ut wisi enim ad minim veniam, quis nostrud exerci tation ullamcorper suscipit lobortis nisl ut aliquip ex ea commodo consequat. Duis autem vel eum iriure dolor in hendrerit in vulputate esse molestie consequat, vel illum dolore eu feugiat nulla facilisis at vero eros et accumsan. Ut wisi enim ad minim veniam, quis nostrud exerci ullamcorper suscipit lobortis nisl ut aliquip ex ea commodo consequat. Duis autem vel eum iriure dolor in hendrerit in vulputate esse molestie consequat, vel illum dolore eu feugiat nulla facilisis at vero eros et accumsan.</p>
    <div class="why-photo"><div role="img" aria-label="Photo of a gardener kneeling among green shrubs"></div></div>
  </div>
</section>

<section>
  <h2 class="abs section-title" style="top:2512px">TESTIMONIALS</h2>
  <p class="abs section-sub" style="top:2565px">Active investment management tailored to your unique needs and goals</p>
  <p class="abs quote">“ Evergreen Renewal Therapy provides Embryonic Stem Cells and unique protocols to doctors in order to help their patients who face major health conditions as well as individuals who simply wish to stay young and healthy. Over the past five years of development. ”</p>
  <svg class="abs arrow" style="left:116px" width="26" height="60" viewBox="0 0 26 60"><path d="M24 2 L2 30 L24 58" fill="none" stroke="#ccc" stroke-width="2"/></svg>
  <svg class="abs arrow" style="left:1058px" width="26" height="60" viewBox="0 0 26 60"><path d="M2 2 L24 30 L2 58" fill="none" stroke="#ccc" stroke-width="2"/></svg>
  <div class="abs avatar" role="img" aria-label="Portrait photo of the client giving the testimonial"></div>
  <p class="abs person">Miss. Patient Name</p>
</section>

<section class="abs lawn-band" role="img" aria-label="Photo of tall green grass blades along a lawn">
  <h2>LEARN HOW -TO <span>KEEP YOUR LAWN GREEN</span></h2>
  <p>Lorem ipsum, we don't agree.</p>
  <a class="btn-outline" href="#">KNOW MORE</a>
</section>

<footer>
  <div class="abs footer">
    <h5 style="left:112px">Quick Links</h5><span class="rule" style="left:112px;width:170px"></span>
    <ul class="links"><li>Home</li><li>About</li><li>Services</li><li>Testimonials</li><li>Contact</li></ul>

    <h5 style="left:347px">Contact Detail</h5><span class="rule" style="left:347px;width:440px"></span>
    <div class="contact">
      <div class="row"><svg width="12" height="16" viewBox="0 0 12 16"><path d="M6 0a6 6 0 0 1 6 6c0 4-6 10-6 10S0 10 0 6a6 6 0 0 1 6-6z" fill="#ddd"/><circle cx="6" cy="6" r="2" fill="#151515"/></svg><span>210 Orchard Lane, Towson, MD 21204</span></div>
      <div class="row"><svg width="14" height="14" viewBox="0 0 24 24"><path d="M5 2l5 5-3 3a14 14 0 0 0 7 7l3-3 5 5-3 3C10 22 2 14 2 5z" fill="#ddd"/></svg><span style="font-size:14px;color:#ddd">555.014.2290</span></div>
      <div class="row"><svg width="14" height="11" viewBox="0 0 14 11"><rect width="14" height="11" rx="1" fill="#ddd"/><path d="M0 1l7 5 7-5" fill="none" stroke="#151515" stroke-width="1.2"/></svg><span>info@brightfurrowmd.com</span></div>
    </div>
    <div class="map" role="img" aria-label="Map showing the company location"></div>

    <h5 style="left:876px">Newsletter Sign Up</h5>
    <div class="news">
      <p>Stay connected and receive email updates from Us</p>
      <div class="field">Enter your email here</div>
      <div class="submit">SUBSCRIBE</div>
    </div>
  </div>
  <div class="abs footer-bar">
    <div class="social"><span></span><span></span><span></span><span></span><span></span></div>
    <p class="copy">Copyright © 2018 BrightFurrowMD. All Rights Reserved</p>
  </div>
</footer>

</body>
</html>
```